Homepage layout for online ad network

Attached is our Calvrex Media logo and updated brief (I can't seem to delete the old logo and brief, but they're no longer relevant).

This project was originally posted with a different logo and corporate name, but we have decided to stay with our current logo and name and redesign the site.

Your design is for a homepage only - design, no coding (I'll get someone else to take your PSD and code it).

Your homepage will make use of a Flash slider - BUT YOU ARE NOT REQUIRED TO PROVIDE THE FLASH. Instead, simply provide the layout and at least two static examples out of the four different sections that will eventually be in the slider.

Much of this design is based on the design of a competitor (listed in the brief).

Please ask whatever questions you need to in order to clarify instructions.
Updates

Project updated to include new logo (and correspondingly new color scheme).

Brief changed slightly.

Thank you for submitting designs for this project in the past.

After some internal strategy work, we have decided to retain our initial corporate identity, Calvrex Media.

If you have submitted a design for the original brief and are available, please re-work your best prior design to reflect the color scheme in the newly uploaded logo.

Target Market(s)

This site is aimed primarily at young professionals who buy digital media on behalf of large advertisers.

Industry/Entity Type

Media

Requirements
Must have
• modern white space
Should not have
• no Flash outside of slider

```html
<!DOCTYPE html>
<html lang="en">
<head>
<meta charset="utf-8">
<title>Calvrex Media — Homepage</title>
<link rel="stylesheet" href="https://fonts.googleapis.com/css2?family=Arimo:wght@400;700&display=swap">
<style>
  :root {
    --red: #d8261f;
    --red-deep: #b00000;
    --red-soft: #a3393a;
    --ink: #222;
    --grey-text: #555;
    --white: #fff;
    --orange: #e8541c;
    --panel: #f1f1f1;
    --footer: #000;
  }
  * { margin: 0; padding: 0; box-sizing: border-box; }
  html, body { width: 1200px; height: 900px; overflow: hidden; }
  body {
    position: relative;
    font-family: "Arimo", Arial, sans-serif;
    color: var(--ink);
    background: repeating-linear-gradient(45deg, #e4e4e4 0 1px, #fafafa 1px 4px);
  }
  .abs { position: absolute; }

  /* Header */
  .header { left: 0; top: 0; width: 1200px; height: 116px; background: var(--white); border-bottom: 2px dashed #ddd; }
  .brand { left: 172px; top: 26px; display: flex; align-items: center; gap: 14px; }
  .brand-square { width: 56px; height: 56px; background: var(--red); }
  .brand-name { font-size: 34px; line-height: 38px; font-weight: 400; letter-spacing: 5px; color: var(--red); }
  .top-links { left: 816px; top: 50px; font-size: 12px; color: #111; }
  .flag { top: 49px; width: 24px; height: 16px; border: 1px solid #888; }
  .flag-us { left: 1020px; background: repeating-linear-gradient(#c33 0 2px, #fff 2px 4px); }
  .flag-us::before { content: ""; position: absolute; left: 0; top: 0; width: 10px; height: 8px; background: #3a4f9a; }
  .flag-uk { left: 1054px; background: #2c3f8f; }
  .flag-uk::before { content: ""; position: absolute; left: 9px; top: 0; width: 4px; height: 14px; background: #d22; box-shadow: 0 0 0 1px #fff; }
  .flag-uk::after { content: ""; position: absolute; left: 0; top: 5px; width: 22px; height: 4px; background: #d22; box-shadow: 0 0 0 1px #fff; }

  /* Navigation band */
  .nav-band { left: 0; top: 120px; width: 1200px; height: 48px; background: linear-gradient(var(--red-soft) 0 48%, var(--red-deep) 48%); }
  .nav-tab { top: 141px; font-size: 14px; color: var(--white); }
  .nav-tab.is-active { left: 724px; top: 133px; width: 71px; height: 35px; background: linear-gradient(#fff, #e8e8e8); color: #000; padding-top: 8px; text-align: center; }

  /* Slider */
  .stage { left: 0; top: 168px; width: 1200px; height: 310px; background: repeating-linear-gradient(45deg, #262626 0 2px, #1d1d1d 2px 4px); }
  .slider-frame { left: 111px; top: 169px; width: 978px; height: 287px; background: var(--white); box-shadow: 0 4px 6px rgba(0,0,0,.4); }
  .slide-left { left: 117px; top: 175px; width: 529px; height: 274px;
    background: radial-gradient(ellipse at 70% 20%, #f46a3a 0%, #c8200f 35%, #5a0806 75%, #2a0303 100%); }
  .slide-right { left: 646px; top: 175px; width: 437px; height: 274px; background: #1a1a1a; }
  .slide-photo { left: 710px; top: 189px; width: 354px; height: 211px; border: 1px solid #ddd;
    background: linear-gradient(160deg, #b5775a, #d09a7d 55%, #f3e4dc); }
  .slide-ledge { left: 666px; top: 400px; width: 417px; height: 33px; background: #000; }
  .slide-title { left: 162px; top: 242px; font-size: 22px; font-weight: 400; color: var(--white); }
  .slide-copy { left: 160px; top: 273px; font-size: 16px; line-height: 25px; color: var(--white); }
  .btn-more { left: 302px; top: 346px; width: 122px; height: 32px; border-radius: 4px; background: linear-gradient(#fff, #d9d9d9); font-size: 16px; color: #111; text-align: center; line-height: 30px; }
  .arrow { width: 28px; height: 28px; border-radius: 50%; background: radial-gradient(circle at 40% 35%, #f7823f, var(--orange)); border: 1px solid #b53a0c; }
  .arrow-prev { left: 99px; top: 298px; }
  .arrow-next { left: 1072px; top: 291px; }
  .arrow svg { position: absolute; left: 8px; top: 8px; }

  /* Main */
  .main { left: 100px; top: 455px; width: 1000px; height: 375px; background: var(--white); border-bottom: 2px dashed #ddd; }
  .dot { top: 460px; width: 14px; height: 14px; border-radius: 50%; background: var(--red); }
  .dot.is-current { background: #000; }
  .features { left: 108px; top: 570px; width: 651px; height: 229px; border-radius: 6px; background: linear-gradient(#fff, var(--panel)); }
  .section-title { left: 133px; top: 497px; font-size: 29px; font-weight: 400; color: #222; }
  .section-title span { color: var(--red); }
  .section-rule { left: 133px; top: 535px; width: 480px; border-top: 2px dashed #ccc; }
  .section-sub { left: 133px; top: 546px; font-size: 15px; color: var(--grey-text); }
  .card { top: 581px; width: 165px; height: 156px; background: var(--white); border: 1px solid #ccc; box-shadow: 0 6px 4px -3px rgba(0,0,0,.25); }
  .card::before { content: ""; position: absolute; inset: 6px; border: 1px dashed #ddd; }
  .card-img { position: absolute; }
  .caption { top: 753px; font-size: 13px; line-height: 20px; color: #111; }

  /* News */
  .news { left: 786px; top: 498px; width: 302px; height: 301px; border: 1px solid #333; border-radius: 7px; background: linear-gradient(200deg, #fff 0 20%, #ececec 21%, #f5f5f5); }
  .news-icon { left: 801px; top: 506px; width: 40px; height: 34px; background: linear-gradient(#eee, #bbb); border-radius: 2px; }
  .news-title { left: 857px; top: 500px; font-size: 38px; font-weight: 400; color: var(--red); }
  .news-list { left: 804px; top: 546px; width: 269px; font-size: 12px; line-height: 24px; text-align: justify; color: #111; list-style: none; }
  .news-date { color: var(--red-deep); display: block; }

  /* Footer */
  .footer { left: 0; top: 831px; width: 1200px; height: 69px; background: var(--footer); }
  .footer-links { left: 0; top: 855px; width: 1200px; text-align: center; font-size: 12px; color: var(--white); }
  .footer-links .muted { color: #999; }
  .footer-links .sep { margin: 0 9px; }
</style>
</head>
<body>

<header class="abs header"></header>
<div class="abs brand"><span class="brand-square"></span><span class="brand-name">CALVREX<br>MEDIA</span></div>
<nav class="abs top-links">Contact Us | Careers | Client Login</nav>
<div class="abs flag flag-us" role="img" aria-label="US English"></div>
<div class="abs flag flag-uk" role="img" aria-label="UK English"></div>

<div class="abs nav-band"></div>
<div class="abs nav-tab is-active">Beauty</div>
<div class="abs nav-tab" style="left:828px">Cooking</div>
<div class="abs nav-tab" style="left:930px">Parenting</div>
<div class="abs nav-tab" style="left:1040px">Video</div>

<div class="abs stage"></div>
<div class="abs slider-frame"></div>
<div class="abs slide-left" role="img" aria-label="Red light-burst background"></div>
<div class="abs slide-right"></div>
<div class="abs slide-ledge"></div>
<div class="abs slide-photo" role="img" aria-label="Close-up beauty photo of an eye with eyeliner"></div>
<h2 class="abs slide-title">Beauty</h2>
<p class="abs slide-copy">Lorem Ipsum is simply dummy text of<br>the printing and typesetting industry.</p>
<div class="abs btn-more">Learn More</div>
<div class="abs arrow arrow-prev"><svg width="10" height="12"><path d="M8 1 L2 6 L8 11 Z" fill="#fff"/></svg></div>
<div class="abs arrow arrow-next"><svg width="10" height="12"><path d="M2 1 L8 6 L2 11 Z" fill="#fff"/></svg></div>

<div class="abs main"></div>
<div class="abs dot is-current" style="left:562px"></div>
<div class="abs dot" style="left:582px"></div>
<div class="abs dot" style="left:602px"></div>
<div class="abs dot" style="left:622px"></div>

<div class="abs features"></div>
<h1 class="abs section-title"><span>Calvrex</span> Media</h1>
<div class="abs section-rule"></div>
<p class="abs section-sub">Advanced Calvrex Media insights for marketers</p>

<div class="abs card" style="left:143px"><div class="card-img" role="img" aria-label="Two people leaping to form a heart on a beach" style="left:17px;top:25px;width:130px;height:94px;background:linear-gradient(#5d8fc9,#b9d2ea 70%,#e8dcc4 72%)"></div></div>
<div class="abs card" style="left:358px"><div class="card-img" role="img" aria-label="Blue 2010 study report book" style="left:35px;top:22px;width:72px;height:112px;background:linear-gradient(90deg,#2d5f96,#4b7fba)"></div></div>
<div class="abs card" style="left:572px"><div class="card-img" role="img" aria-label="Goldfish jumping between two fishbowls" style="left:10px;top:28px;width:145px;height:118px;background:linear-gradient(#fff,#dbe9f4 60%,#f4f8fb)"></div></div>

<p class="abs caption" style="left:153px">Cohort delivers<br>a 71% ROI. Sweet!</p>
<p class="abs caption" style="left:369px">2010 Display<br>Advertising Study</p>
<p class="abs caption" style="left:582px">Display Advertising<br>Engagement on the Rise</p>

<aside class="abs news"></aside>
<div class="abs news-icon" role="img" aria-label="Newspaper icon"></div>
<h2 class="abs news-title">News</h2>
<ul class="abs news-list">
  <li><span class="news-date">September 29, 2010</span>Cohort Media does a good job of homepage design</li>
  <li><span class="news-date">September 24, 2010</span>Giving the brand the right audience</li>
  <li><span class="news-date">September 16, 2010</span>Cohort Launches in the UK</li>
  <li><span class="news-date">September 8, 2010</span>Cohort Taps Vantro, Beamcast, Pivot, and Clipwave</li>
</ul>

<footer class="abs footer"></footer>
<nav class="abs footer-links"><span class="muted">About us</span><span class="sep">|</span>Contact Us<span class="sep">|</span>Management Team<span class="sep">|</span>News<span class="sep">|</span>Careers</nav>

</body>
</html>
```